Financial Services - Brochure for Mortgage Brokers to use with Borrowers

******** Modification - based on the designs we have received to date we have decided to go with 11x17" (4 faces) that will be folded into 8.5x11 - we have too much information for the smaller tri-fold format. ***************

We need to develop a tool for mortgage brokers (our distribution channel) to use with borrowers to make selling our services easier.

Our brochure will be in both english and french (probably 2 separate units due to length) (to date our collateral materials have been one page recto-verso with english on one side and french on the other side).

We already have a layout that we use - see examples for existing layout and design format (i will upload the: 1) 8.5'x11' single page flyer with english on e side and french the other side 2) the 10 questions unit we use 4.5"x11")

I have prepared a powerpoint which I will upload that shows the objectives and provides content examples.

The final product we are looking for is in English, we would then provide the french text to add to the 2nd unit.

Reason: I have been traveling and not able to respond to submissions. I would like to provide time for feedback.

Clarification:

We are open to 2 formats: either 8.5x11" trifold or 11x17" brochure (4 faces) format. 

Reason: Still traveling and need time to finalize feedback - thank you

Target Market(s)

Borrowers (consumers) who are having financial difficulties and as a result may lose their homes - they are in a high state of emotional crisis and need someone to "take charge (broker)" and be walked thru a plan (our brochure that you will be creating)

Industry/Entity Type

Financial

Requirements
Must have
• Must be consistent with our current look and feel (ie colours, professionalism)

Must be easy to produce as we will do short runs and have the brochures printed with our different broker's contact info on the back - so either a trifold 8.5"x11" or a 11x17"

```html
<!DOCTYPE html>
<html lang="en">
<head>
<meta charset="utf-8">
<title>VALMER Finance – Short Term Mortgage Solutions Brochure</title>
<link rel="stylesheet" href="https://fonts.googleapis.com/css2?family=Open+Sans:ital,wght@0,400;0,600;0,700;1,600&family=Open+Sans+Condensed:wght@700&display=swap">
<style>
:root{
  --purple:#685c92;
  --purple-mid:#8479aa;
  --purple-soft:#a59dc4;
  --lavender:#dcd8ea;
  --line-blue:#9fb3c3;
  --text-grey:#8c8c98;
  --text-dark:#5c5a6e;
  --sidebar:#e4e7ea;
  --white:#ffffff;
  --page-bg:#ffffff;
}
*{box-sizing:border-box;margin:0;padding:0}
html,body{width:927px;height:1200px;overflow:hidden;background:var(--page-bg)}
body{position:relative;font-family:"Open Sans",sans-serif;color:var(--text-grey)}
.panel{position:absolute;overflow:hidden;background:var(--white);box-shadow:2px 3px 4px rgba(0,0,0,.35)}
.panel svg.bg{position:absolute;left:0;top:0}
.abs{position:absolute}
.heading{font-family:"Open Sans Condensed","Open Sans",sans-serif;font-weight:700;text-transform:uppercase;letter-spacing:.1px}
.brand-name{font-family:"Open Sans",sans-serif;font-weight:400;color:var(--purple);letter-spacing:6px}
.tagline{font-style:italic;font-weight:600;color:var(--white);line-height:1;text-align:right;text-shadow:0 1px 2px rgba(0,0,0,.25)}

/* back cover */
.back{left:18px;top:22px;width:447px;height:568px}
.back .strategy-title{left:27px;top:55px;font-size:9.5px;color:var(--lavender)}
.back .stage-label{font-size:7px;color:var(--white);line-height:1.1}
.back .duration{font-size:7px;color:var(--lavender);top:161px}
.back .cost-title{left:27px;top:197px;font-size:9px;color:var(--lavender)}
.back .chart-label{font-size:7px;color:var(--lavender);text-align:center;line-height:1.2}
.back .axis-label{font-size:4.5px;color:var(--lavender)}
.back .brand-block{left:26px;top:485px}
.back .brand-block .brand-name{font-size:26px}
.back .company{left:26px;top:534px;font-size:8px;line-height:1.35}
.back .company b{color:#8a9aa8;font-weight:600}
.back .contact{left:315px;top:511px;font-size:8px;line-height:1.35}
.back .contact b{color:var(--purple);font-weight:700}

/* front cover */
.front{left:465px;top:22px;width:448px;height:568px}
.front .brand-block{left:258px;top:80px;display:flex;align-items:center;gap:8px}
.front .brand-mark{width:10px;height:10px;border-radius:50%;background:var(--purple-mid)}
.front .brand-name{font-size:34px}
.front .tagline{right:72px;top:252px;font-size:17px}
.front .cover-title{right:38px;top:469px;font-size:14.5px;color:var(--lavender)}

/* inside left */
.inside-left{left:18px;top:614px;width:447px;height:569px}
.inside-left .tagline{left:38px;top:62px;width:200px;font-size:17px}
.col-head{font-size:6.5px;color:var(--purple);font-weight:700;text-transform:uppercase;line-height:1.15}
.col-list{font-size:6.5px;line-height:1.25;color:var(--text-grey);list-style:none}
.col-list li::before{content:"• "}
.solution-list{font-size:6.5px;line-height:1.25;color:var(--text-grey);list-style:none}
.solution-list li::before{content:"• "}
.solution-list .lead{color:var(--text-dark);font-weight:700}
.solution-list .lead::before{content:""}
.steps-table{position:absolute;left:34px;top:289px;width:387px;border-collapse:collapse;font-size:6.4px;line-height:1.25}
.steps-table th{height:29px;color:var(--white);font-weight:700;text-transform:uppercase;font-size:6.2px;vertical-align:middle}
.steps-table th.step-col{width:68px;text-align:left;padding-left:4px;line-height:1.15}
.steps-table td{border-top:1px solid #c9c6d6;padding:3px 4px;vertical-align:top}
.steps-table td.step{background:var(--lavender);color:var(--purple);font-size:6.8px;line-height:1.2}
.steps-table td.example{background:var(--white);color:var(--text-grey)}
.steps-table td.example span{display:block}

/* inside right */
.inside-right{left:465px;top:614px;width:448px;height:569px}
.inside-right .sidebar{left:292px;top:0;width:156px;height:569px;background:var(--sidebar)}
.sec-title{font-size:8.6px;color:var(--purple)}
.impact-text{left:27px;top:72px;width:250px;font-size:7.2px;line-height:1.6;text-transform:uppercase;color:var(--text-grey)}
.market-label{font-size:6.6px;color:var(--white);line-height:1.2}
.philosophy-box{position:absolute;width:62px;height:85px;border:1px solid var(--purple-soft);border-radius:6px;background:var(--white);text-align:center;font-size:6.3px;color:var(--text-grey);line-height:1.45;padding-top:22px}
.philosophy-box .mini-brand{position:absolute;left:0;right:0;top:9px;font-size:5px;color:var(--purple);letter-spacing:1px;line-height:1}
.philosophy-box svg{position:absolute;left:50%;bottom:6px;transform:translateX(-50%)}
.check-list{list-style:none;font-size:5.7px;line-height:1.22;color:var(--text-grey)}
.check-list li{padding-left:7px;position:relative}
.check-list li::before{content:"✓";position:absolute;left:0;color:var(--purple)}
.check-list li.indent{padding-left:14px}
.check-list li.indent::before{content:""}
</style>
</head>
<body>

<!-- ===== BACK COVER ===== -->
<section class="panel back">
  <svg class="bg" width="447" height="568" viewBox="0 0 447 568">
    <defs>
      <linearGradient id="handshakeTone" x1="0" y1="0" x2="0" y2="1">
        <stop offset="0" stop-color="#a9bcd6"/>
        <stop offset=".45" stop-color="#d9b8a4"/>
        <stop offset="1" stop-color="#7b8da0"/>
      </linearGradient>
    </defs>
    <rect width="447" height="380" fill="var(--purple)"/>
    <circle cx="470" cy="190" r="185" fill="url(#handshakeTone)" role="img" aria-label="Photo of a business handshake in front of a house"/>
    <path d="M0 372 Q220 352 447 362 L447 568 L0 568 Z" fill="var(--white)"/>
    <path d="M0 372 Q220 352 447 362" fill="none" stroke="var(--line-blue)" stroke-width="3"/>
    <!-- graduation arcs -->
    <g fill="none" stroke="var(--lavender)" stroke-width="1.2">
      <path d="M48 112 Q50 70 130 72 Q240 72 248 112"/>
      <path d="M80 112 Q90 88 120 90 Q140 92 142 112"/>
      <path d="M160 112 Q175 88 205 90 Q225 92 228 112"/>
    </g>
    <g fill="var(--lavender)">
      <path d="M244 108 l4 6 l4 -6 z"/><path d="M138 108 l4 6 l4 -6 z"/><path d="M224 108 l4 6 l4 -6 z"/>
    </g>
    <path d="M132 88 l10 -5 l10 5 l-10 5 z M136 90 v5 q6 4 12 0 v-5" fill="var(--lavender)"/>
    <!-- stage chevrons -->
    <polygon points="26,118 104,118 112,136 104,155 26,155" fill="var(--lavender)" opacity=".95"/>
    <polygon points="108,118 188,118 196,136 188,155 108,155 116,136" fill="var(--purple-soft)"/>
    <polygon points="192,118 278,118 286,136 278,155 192,155 200,136" fill="var(--purple-mid)"/>
    <!-- cost chart -->
    <g stroke="var(--purple-soft)" stroke-width=".8" fill="none">
      <line x1="30" y1="225" x2="30" y2="348"/>
      <line x1="30" y1="348" x2="245" y2="348"/>
    </g>
    <path d="M62 252 Q140 260 182 318" fill="none" stroke="var(--lavender)" stroke-width="5"/>
    <polygon points="170,320 193,338 188,310" fill="var(--lavender)"/>
  </svg>

  <div class="abs heading strategy-title">VALMER's Graduation Strategy</div>
  <div class="abs stage-label" style="left:36px;top:127px;width:66px">VALMER Short Term Solutions</div>
  <div class="abs stage-label" style="left:133px;top:132px">Hearth Trust</div>
  <div class="abs stage-label" style="left:210px;top:127px;width:70px">"A" Banks, Insurance Co .....</div>
  <div class="abs duration" style="left:42px">6 to12 months</div>
  <div class="abs duration" style="left:124px">12 to18 months</div>
  <div class="abs duration" style="left:218px">300 months</div>
  <div class="abs heading cost-title">How to lower your long-termcost of borrowing with VALMER</div>
  <div class="abs axis-label" style="left:14px;top:232px;transform:rotate(-90deg)">Rate %</div>
  <div class="abs axis-label" style="left:228px;top:340px">TIME</div>
  <div class="abs chart-label" style="left:110px;top:247px">Solutions VALMER (6 - 12 months)</div>
  <div class="abs chart-label" style="left:168px;top:271px">Hearth Trust<br>(12 to 18 months)</div>
  <div class="abs chart-label" style="left:208px;top:304px">"A" Institutions<br>(300 months)</div>

  <div class="abs brand-block"><span class="brand-name">VALMER</span></div>
  <div class="abs company">VALMER Finance<br><b>www.valmerfinance.com</b></div>
  <div class="abs contact"><b>CONTACT</b><br>Alex Martin<br>Phone: 555-555-0148<br>alex@example.com</div>
</section>

<!-- ===== FRONT COVER ===== -->
<section class="panel front">
  <svg class="bg" width="448" height="568" viewBox="0 0 448 568">
    <defs>
      <linearGradient id="coupleTone" x1="0" y1="0" x2="1" y2="1">
        <stop offset="0" stop-color="#e4ded2"/>
        <stop offset=".5" stop-color="#b79a80"/>
        <stop offset="1" stop-color="#d8cbb2"/>
      </linearGradient>
    </defs>
    <path d="M0 198 Q200 168 448 182 L448 380 L0 380 Z" fill="url(#coupleTone)" role="img" aria-label="Photo of a couple embracing in front of their home"/>
    <path d="M0 198 Q200 168 448 182" fill="none" stroke="var(--line-blue)" stroke-width="3"/>
    <path d="M0 378 Q220 358 448 372 L448 568 L0 568 Z" fill="var(--purple)"/>
    <path d="M0 378 Q220 358 448 372" fill="none" stroke="var(--line-blue)" stroke-width="3"/>
  </svg>
  <div class="abs brand-block"><span class="brand-mark"></span><span class="brand-name">VALMER</span></div>
  <div class="abs tagline">Funding to achieve<br>&nbsp;&nbsp;&nbsp;&nbsp;&nbsp;your goals...™</div>
  <div class="abs heading cover-title">Short Term Mortage Solutions</div>
</section>

<!-- ===== INSIDE LEFT ===== -->
<section class="panel inside-left">
  <svg class="bg" width="447" height="569" viewBox="0 0 447 569">
    <defs>
      <linearGradient id="skyTone" x1="0" y1="0" x2="0" y2="1">
        <stop offset="0" stop-color="#7ea2cf"/>
        <stop offset=".55" stop-color="#cfdcec"/>
        <stop offset="1" stop-color="#ffffff"/>
      </linearGradient>
      <radialGradient id="handTone" cx=".5" cy=".5" r=".5">
        <stop offset="0" stop-color="#d9a98f"/>
        <stop offset=".6" stop-color="#e6c3b0" stop-opacity=".8"/>
        <stop offset="1" stop-color="#ffffff" stop-opacity="0"/>
      </radialGradient>
    </defs>
    <rect width="447" height="170" fill="url(#skyTone)" role="img" aria-label="Photo of a sky with a hand sheltering a small model house"/>
    <ellipse cx="330" cy="110" rx="130" ry="95" fill="url(#handTone)"/>
    <path d="M0 292 Q220 270 447 276 L447 569 L0 569 Z" fill="var(--purple)"/>
    <path d="M0 292 Q220 270 447 276" fill="none" stroke="var(--line-blue)" stroke-width="3"/>
  </svg>
  <div class="abs tagline">Funding to achieve<br>your goals...™</div>

  <div class="abs col-head" style="left:39px;top:158px">Life happens</div>
  <div class="abs col-head" style="left:127px;top:151px;width:80px">Creates financial crisis situations</div>
  <div class="abs col-head" style="left:214px;top:158px">Solution</div>
  <svg class="abs" style="left:39px;top:169px" width="195" height="2"><line x1="0" y1="1" x2="195" y2="1" stroke="var(--purple)" stroke-width=".6"/></svg>
  <ul class="abs col-list" style="left:39px;top:184px;width:80px">
    <li>Divorce</li><li>Loss of job</li><li>Sickness/health</li><li>Unforeseen<br>&nbsp;&nbsp;circumstances</li><li>Starting a new<br>&nbsp;&nbsp;business</li>
  </ul>
  <ul class="abs col-list" style="left:127px;top:184px;width:86px">
    <li>Notice of assessment<br>&nbsp;&nbsp;(NOA) not paid</li><li>Legal mortgage</li><li>Unpaid property taxes</li><li>Crack in the house<br>&nbsp;&nbsp;foundation</li><li>Construction lien</li><li>Less than 2 years in<br>&nbsp;&nbsp;business-for-self (BFS)</li><li>60 day notice</li>
  </ul>
  <ul class="abs solution-list" style="left:214px;top:184px;width:95px">
    <li class="lead">Use the Equity<br>in your home to:</li>
    <li>solve the current<br>&nbsp;&nbsp;"financial crisis"</li>
    <li>Develop and fund a<br>&nbsp;&nbsp;plan to put you back<br>&nbsp;&nbsp;on a solid financial<br>&nbsp;&nbsp;footing and in good<br>&nbsp;&nbsp;standing</li>
  </ul>

  <table class="steps-table">
    <thead>
      <tr><th class="step-col">Steps to solving the "financial crisis"</th><th>Examples</th></tr>
    </thead>
    <tbody>
      <tr style="height:54px"><td class="step">Build your "Power Team"</td><td class="example"><span>• Mortgage Broker (quarterback)</span><span>• Private Lender</span><span>• Real estate agent</span><span>• Notary</span><span>• Lawyer Trustee</span></td></tr>
      <tr style="height:27px"><td class="step">Identify problem</td><td class="example"><span>• Lost my job and fell behind on the mortgage payments which led to a 60 day notice and now</span><span>&nbsp;&nbsp;no Bank will refinance me we will lose my house</span></td></tr>
      <tr style="height:41px"><td class="step">Identify causes of the problem</td><td class="example"><span>• Cashflow dries up</span><span>• Too much debt with high interest rates strangling cashflow</span><span>• Credit score too low</span><span>• Too much debt hurts credit score</span></td></tr>
      <tr style="height:27px"><td class="step">Create Budget</td><td class="example"><span>• Determine how paying off high interest rate debts will improve cashflow</span><span>• Good vs bad debts / Discipline</span></td></tr>
      <tr style="height:33px"><td class="step">Credit Repair plan</td><td class="example"><span>• Payoff certain debts</span><span>• Lower balances on certain debts</span><span>• New credit card</span></td></tr>
      <tr style="height:39px"><td class="step">Remedy the "financial crisis"</td><td class="example"><span>• Pay off the cause of the "financial crisis" ie 60 day notice, legal mortgage</span><span>• Debt consoidation</span></td></tr>
    </tbody>
  </table>
</section>

<!-- ===== INSIDE RIGHT ===== -->
<section class="panel inside-right">
  <div class="abs sidebar"></div>
  <svg class="bg" width="448" height="569" viewBox="0 0 448 569">
    <defs>
      <linearGradient id="homeTone" x1="0" y1="0" x2="0" y2="1">
        <stop offset="0" stop-color="#c8dcec"/>
        <stop offset=".55" stop-color="#a8a59c"/>
        <stop offset="1" stop-color="#6f9a4d"/>
      </linearGradient>
    </defs>
    <path d="M0 362 Q220 338 448 350 L448 569 L0 569 Z" fill="url(#homeTone)" role="img" aria-label="Photo of a stone family house with a hand holding out house keys"/>
    <!-- market chevrons -->
    <polygon points="27,158 108,158 116,173 108,188 27,188" fill="var(--purple)"/>
    <polygon points="112,158 192,158 200,173 192,188 112,188 120,173" fill="var(--purple-mid)"/>
    <polygon points="196,158 276,158 284,173 276,188 196,188 204,173" fill="var(--purple-soft)"/>
    <!-- two-way arrow -->
    <line x1="104" y1="262" x2="154" y2="262" stroke="var(--purple)" stroke-width="1"/>
    <path d="M104 262 l5 -3 v6 z M154 262 l-5 -3 v6 z" fill="var(--purple)"/>
  </svg>

  <div class="abs heading sec-title" style="left:27px;top:52px">Impact of not resolving the "financial crisis"</div>
  <div class="abs impact-text">Lose your home • Lose your equity in the home • Long term blemish on your credit report • Possible judgments leading to seizure • Loss of credibility • Serious family pressure • Shame</div>
  <div class="abs heading sec-title" style="left:27px;top:138px">The residential mortgage market</div>
  <div class="abs market-label" style="left:38px;top:162px">Private Lenders<br>(ie. VALMER Finance)</div>
  <div class="abs market-label" style="left:124px;top:162px">Alternative Lenders<br>(ie Hearth Trust)</div>
  <div class="abs market-label" style="left:208px;top:162px">"A" Banks, Insurance<br>Companies et al</div>
  <div class="abs heading sec-title" style="left:32px;top:212px">Private lender philosophies where does VALMER fit?</div>

  <div class="philosophy-box" style="left:29px;top:231px">REPOSSESS<br>AND<br>LOSE HOME
    <svg width="30" height="22" viewBox="0 0 30 22"><path d="M2 11 L13 2 L24 11 H21 V21 H5 V11 Z" fill="var(--purple)"/><rect x="14" y="12" width="14" height="7" fill="var(--white)" stroke="var(--purple)" stroke-width=".8"/></svg>
  </div>
  <div class="philosophy-box" style="left:166px;top:231px"><span class="mini-brand">VALMER</span>REPAY<br>&amp; GRADUATE
    <svg width="36" height="20" viewBox="0 0 36 20"><path d="M1 10 L10 2 L19 10 H16 V19 H4 V10 Z" fill="var(--purple)"/><path d="M20 9 l7 -4 l7 4 l-7 4 z M23 11 v5 q4 3 8 0 v-5" fill="var(--purple)"/></svg>
  </div>

  <div class="abs heading sec-title" style="left:300px;top:51px">Private lending perceptions</div>
  <ul class="abs check-list" style="left:300px;top:63px;width:145px">
    <li>Too expensive</li><li>Lack transparency</li><li>Poor ethics</li><li>Difficult to do business with and to get</li><li class="indent">a deal done</li><li>Hard to sell to "my client"</li><li>Funding</li><li>Do they have sufficient funds</li><li>Where do their funds come from</li><li>Will they actually fund the deal or is my</li><li class="indent">client left hanging</li><li>Promises are broken</li><li>The borrowers will be poorly treated</li><li class="indent">when there is a default</li><li>Focus is on repossession vs repayment</li>
  </ul>
  <div class="abs heading sec-title" style="left:300px;top:208px">New paradigm in private lending</div>
  <ul class="abs check-list" style="left:300px;top:220px;width:145px">
    <li>Affordable</li><li>Transparent</li><li>Ethical</li><li>Easy to do business with and to get</li><li class="indent">a deal done</li><li>Can sell to "my client"</li><li>Funding</li><li>Sufficient funds</li><li>Legitimate source of funds</li><li>Get deals done – no one left hanging</li><li>Promises are kept</li><li>The borrowers will be treated with</li><li class="indent">professionalism when there is a default</li><li>Focus is on repayment and graduation</li>
  </ul>
</section>

</body>
</html>
```